GRAPHICS FOR AN ICO WHITE PAPER DOCUMENT

For a new ICO launch of a Token on Blockchain, we need a new graphical setup of the White Paper document.
Consider that we want high impact in order to introduce the financial project, with several schemes, tables and graphs.
The actual logos are different and are provided attached.
Please send the first page as an example, an internal page, a sample of the argument list (in the final version they must be cliikable for fast moving inside the document), put the logo even small in every page and home button to get back to beginning. COMMENTS AND SUGGESTIONS ARE WELCOME WE WILL NEED CONTINUOUS COOPERATION WITH THE WINNER.

Target Market(s)

Investment, finance, blockchain

Industry/Entity Type

Investment Advisory

Font styles to use
Serif
Sans Serif
Decorative

Colors

Designer to choose colors to be used in the design.

Requirements
Must have
• End version in PDF small size, character size 15, distintive modern, neat look but dinamic, with right and left pages with different design, show movement of text between pages.
• Graphs, tables, easy to read and nice to see.
Nice to have
• EASY TO READ AND NAVIGATE
Should not have
• NO BORING STUFF!!!

```html
<!DOCTYPE html>
<html lang="en">
<head>
<meta charset="utf-8">
<title>QVX Security Token Offering Whitepaper – Spread 8–9</title>
<link href="https://fonts.googleapis.com/css2?family=Exo+2:wght@400;500;600;700&display=swap" rel="stylesheet">
<style>
  :root{
    --navy:#1b2a44;
    --navy-deep:#14213a;
    --blue:#1e3f9f;
    --blue-mid:#2d58b8;
    --ink:#1a1a1a;
    --muted:#333;
    --paper:#ffffff;
    --panel:#eceef1;
    --row-blue:#acd4e8;
    --row-hi:#91d2ef;
    --row-net:#b7c4ad;
    --row-ratio:#72bcdc;
    --rule:#8a8f96;
  }
  *{box-sizing:border-box;margin:0;padding:0}
  html,body{width:1200px;height:848px;overflow:hidden;background:#fff}
  body{font-family:"Exo 2",sans-serif;color:var(--ink)}
  .spread{position:relative;width:1200px;height:848px;overflow:hidden;background:var(--paper)}
  .page{position:absolute;top:0;height:848px}
  .page-left{left:0;width:598px;background:linear-gradient(90deg,#fff 0%,#fff 93%,#e4e4e4 98%,#c9c9c9 100%)}
  .page-right{left:598px;width:602px;background:linear-gradient(90deg,#bdbdbd 0%,#e6e6e6 2%,#fff 6%,#fff 100%)}

  .folio{position:absolute;top:0;width:36px;height:35px;background:var(--blue);color:#fff;font-size:14px;display:flex;align-items:center;justify-content:center}
  .page-left .folio{left:0}
  .page-right .folio{left:2px}

  .running-head{position:absolute;top:12px;font-size:9.5px;color:var(--ink)}
  .brand{position:absolute;left:60px;top:9px;display:flex;align-items:center;gap:5px;font-size:17px;font-weight:700;color:var(--blue)}
  .brand-dot{width:14px;height:14px;border-radius:50%;background:var(--blue)}

  .section-tab{position:absolute;left:0;background:#111;color:#fff;font-size:17px;font-weight:500;height:28px;display:flex;align-items:center;justify-content:flex-end;padding-right:22px}
  .sub-tab{position:absolute;left:0;height:27px;width:168px;background:linear-gradient(90deg,#3a63c2,var(--blue));color:#fff;font-size:16px;display:flex;align-items:center;padding-left:60px}

  .problem-box{position:absolute;left:36px;top:64px;width:528px;height:206px;background:linear-gradient(90deg,var(--navy-deep),var(--navy) 85%,#5f7898 100%);box-shadow:0 3px 6px rgba(0,0,0,.3);color:#fff;padding:38px 40px 0 24px;font-size:14.3px;line-height:17px}
  .problem-box p+p{margin-top:17px}

  .solution-panel{position:absolute;left:0;top:314px;width:596px;height:350px;background:linear-gradient(180deg,#fff 0%,#f2f3f5 40%,#e3e5e8 100%);box-shadow:0 3px 4px rgba(0,0,0,.12)}
  .solution-lead{position:absolute;left:60px;top:327px;width:470px;font-size:12.6px;font-weight:700;line-height:16px}
  .body-copy{position:absolute;left:60px;width:470px;font-size:11.8px;line-height:14.5px;color:var(--muted)}
  .body-copy p+p{margin-top:14.5px}

  .formula-list{position:absolute;left:60px;top:720px;width:480px;font-size:11.8px;line-height:14.5px;color:var(--muted);list-style:none}

  .foot-band{position:absolute;bottom:0;height:10px}

  .pl-table{position:absolute;left:50px;top:112px;width:502px;border-collapse:collapse;table-layout:fixed;font-size:9.6px}
  .pl-table col.label{width:109px}
  .pl-table th{background:var(--blue);color:#fff;font-weight:600;text-align:left;padding:0 7px;height:22px;font-size:10.5px;border-left:1px solid #fff}
  .pl-table th:first-child{background:transparent;border:0}
  .pl-table td{padding:3px 7px 0;vertical-align:top;border-bottom:1px solid var(--rule);border-left:1px solid var(--rule);height:21.6px;line-height:11.5px}
  .pl-table td:first-child{border-left:0}
  .pl-table tr.tall td{height:33.6px}
  .pl-table tr.alt td{background:var(--row-blue)}
  .pl-table tr.key td{background:var(--row-hi);font-weight:700}
  .pl-table tr.bold td{font-weight:700}
  .pl-table tr.net td{background:var(--row-net);font-weight:700}
  .pl-table tr.ratio td{background:var(--row-ratio);font-weight:700;border-bottom:0}
  .pl-table td.group{background:var(--blue);color:#fff;font-weight:600}
</style>
</head>
<body>
<div class="spread">

  <section class="page page-left">
    <div class="folio">8</div>
    <div class="brand"><span class="brand-dot"></span>QVX</div>
    <div class="running-head" style="left:144px">Security Token Offering Whitepaper</div>
    <div class="running-head" style="left:378px">August 2018</div>
    <div class="running-head" style="left:504px;top:11px">Luca Bernardi</div>

    <div class="section-tab" style="top:36px;width:212px">Opportunity</div>
    <div class="problem-box">
      <p>Investors and money managers want an increased return on investment with a minimal amount of added risk, at the same time that the investment opportunity landscape is fast-changing and becoming more complex every day.</p>
      <p>Recent developments in Blockchain technology, alongside with Artificial Intelligence and Broadband Internet have created the possibility to create new systems of trading capable of achieving the best equilibrium between the risk and reward.</p>
    </div>
    <div class="sub-tab" style="top:64px">Problem</div>

    <div class="solution-panel"></div>
    <div class="sub-tab" style="top:286px;height:28px">Solution</div>
    <p class="solution-lead">The solution is to have a personal fund managed in the most professional and advanced way possible.</p>
    <div class="body-copy" style="top:372px">
      <p>QVX has developed an advanced Trading System Software called <b>PATS (Precision Adaptive Trading System)</b> based on Technical Analysis, Statistics, Artificial Intelligence, and Quantitative Analysis. QVX is creating a breakthrough blockchain-based indicator named the <b>QVX Sentiment Index</b> that will add a unique, transparent, and reliable market indicator to PATS. Our index will establish an understanding of people's attitude towards financial market trends at any given moment, worldwide.</p>
      <p>QVX PATS is not a single trading system; rather, it is the sum of four different trading systems, each one with its own characteristics and specific risk/reward strengths. Added to this, QVX will insert an indicator created on the blockchain by its token</p>
      <p>QVX Sentiment Index is an indicator based on pure feelings of people for specific markets or instruments negotiated in a given moment, worldwide.</p>
      <p>QVX does not require any upfront price for its PATS license: it bases all its remuneration to results granted for real by its PATS at customer portfolios. This offers tremendous opportunity for value creation in the long term, and, at the same time, lowers entry barriers so that customers pay only when they make a profit.</p>
    </div>

    <div class="sub-tab" style="top:682px;height:28px">Formula</div>
    <ul class="formula-list">
      <li>• expected average return per annum of PATS on third-party Assets under management = 21%</li>
      <li>• expected average fee on the 21% = 20%</li>
      <li>• net fee on Asset Under management of Institutional customers 4.2%</li>
      <li>MARKET</li>
      <li>QVX operates in the Alternative Investment Fund industry that manages $3.5 Trillion</li>
    </ul>

    <div class="foot-band" style="left:0;width:168px;background:var(--blue)"></div>
    <div class="foot-band" style="left:168px;width:430px;background:var(--navy)"></div>
  </section>

  <section class="page page-right">
    <div class="folio">9</div>
    <div class="section-tab" style="top:36px;left:2px;width:212px;padding-right:38px">Financing</div>
    <div class="sub-tab" style="top:64px;left:2px;width:250px;height:32px;padding-left:58px;font-size:16.5px">Projected Profit and Loss</div>

    <table class="pl-table">
      <colgroup><col class="label"><col><col><col><col><col></colgroup>
      <thead>
        <tr><th></th><th>2019</th><th>2020</th><th>2021</th><th>2022</th><th>2023</th></tr>
      </thead>
      <tbody>
        <tr class="bold"><td>Revenue</td><td>€30,606,003</td><td>€57,509,905</td><td>€103,917,839</td><td>€191,702,920</td><td>€420,615,717</td></tr>
        <tr class="alt bold"><td>Direct Costs</td><td>€18,049,904</td><td>€26,745,586</td><td>€42,106,219</td><td>€71,985,501</td><td>€149,614,255</td></tr>
        <tr><td></td><td></td><td></td><td></td><td></td><td></td></tr>
        <tr class="alt"><td><b>Gross Margin</b></td><td>€12,556,099</td><td>€30,764,320</td><td>€61,811,620</td><td>€119,717,419</td><td>€271,001,461</td></tr>
        <tr class="bold"><td>Gross Margin %</td><td>41%</td><td>53%</td><td>59%</td><td>62%</td><td>64%</td></tr>
        <tr><td class="group">Operating Expenses</td><td></td><td></td><td></td><td></td><td></td></tr>
        <tr><td>Salaries &amp; Wages</td><td>€1,443,000</td><td>€2,712,000</td><td>€3,997,200</td><td>€6,151,584</td><td>€9,135,618</td></tr>
        <tr class="alt tall"><td>Employee Related Expenses</td><td>€152,100</td><td>€302,040</td><td>€469,116</td><td>€762,260</td><td>€1,174,894</td></tr>
        <tr><td>OFFICES</td><td>€99,000</td><td>€192,000</td><td>€240,000</td><td>€300,000</td><td>€300,000</td></tr>
        <tr class="alt"><td>Bills</td><td>€31,400</td><td>€48,000</td><td>€54,000</td><td>€60,000</td><td>€72,000</td></tr>
        <tr><td>WEB Servers</td><td>€57,000</td><td>€96,000</td><td>€144,000</td><td>€192,000</td><td>€240,000</td></tr>
        <tr class="alt tall"><td>Accountancy and KYC and AML</td><td>€54,000</td><td>€100,000</td><td>€140,000</td><td>€160,000</td><td>€200,000</td></tr>
        <tr class="tall"><td>Transfers and General exp.</td><td>€52,000</td><td>€108,000</td><td>€144,000</td><td>€160,000</td><td>€180,000</td></tr>
        <tr class="alt"><td>Cars and Fringes</td><td>€39,200</td><td>€48,000</td><td>€60,000</td><td>€80,000</td><td>€100,000</td></tr>
        <tr><td>MARKETING</td><td>€1,600,000</td><td>€4,400,000</td><td>€7,700,000</td><td>€12,500,000</td><td>€19,500,000</td></tr>
        <tr class="alt tall"><td>Customer Service and Activation</td><td>€1,200,000</td><td>€2,400,000</td><td>€4,000,000</td><td>€8,000,000</td><td>€12,000,000</td></tr>
        <tr class="key tall"><td>Total Operating Expenses</td><td>€4,727,700</td><td>€10,406,040</td><td>€16,948,316</td><td>€28,365,844</td><td>€42,902,512</td></tr>
        <tr><td></td><td></td><td></td><td></td><td></td><td></td></tr>
        <tr class="key"><td>Operating Income</td><td>€7,828,399</td><td>€20,358,279</td><td>€44,863,304</td><td>€91,351,575</td><td>€228,098,949</td></tr>
        <tr><td></td><td></td><td></td><td></td><td></td><td></td></tr>
        <tr><td>Interest Incurred</td><td></td><td></td><td></td><td></td><td></td></tr>
        <tr class="alt tall"><td>Depreciation and Amortization</td><td>€504,651</td><td>€545,873</td><td>€618,161</td><td>€676,579</td><td>€750,849</td></tr>
        <tr><td>Income Taxes</td><td>€2,563,312</td><td>€6,934,342</td><td>€15,485,800</td><td>€31,736,249</td><td>€79,571,835</td></tr>
        <tr class="key"><td>Total Expenses</td><td>€25,845,567</td><td>€44,631,841</td><td>€75,158,495</td><td>€132,764,174</td><td>€272,839,452</td></tr>
        <tr class="net"><td>Net Profit</td><td>€4,760,436</td><td>€12,878,064</td><td>€28,759,344</td><td>€58,938,746</td><td>€147,776,265</td></tr>
        <tr class="ratio"><td>Net Profit / Sales</td><td>16%</td><td>22%</td><td>28%</td><td>31%</td><td>35%</td></tr>
      </tbody>
    </table>

    <div class="foot-band" style="left:0;width:602px;background:var(--navy)"></div>
  </section>

</div>
</body>
</html>
```